Create Stationary from existing logo(s)

We are looking for some assistance in tidying up the stationary that supports our brand. We are an innovative technology company, generally working with larger corporates. We have previously done a little work on brochures etc, but never really pulled it all together with our stationary.
In particular I am looking for:
1. A4 Letter Template for Letter (Microsoft Word 2007 template format)
2. A4 Template for Reports (Microsoft Word 2007 template format). This should include title page, table of contents, subsequent report pages including styles for tables, headings, and text.
3. Business Card Design - we will need to be able to edit the text, so the card should include sample text for name, title, phone number, mobile number, and email address.
4. Presentation Template (Microsoft Powerpoint 2007 template). See attached powerpoint which we quite like, but isn't really a template, and we have don't really use any consistent styles in it. The Powerpoint template needs to have a cover / title page, section break pages, and pages that may contain bullet point text, pictures, or a combination of bullet point text and pictures. We do like our current presentation, which gives some indication of our thinking.
I am attaching a brochure and the powerpoint presentation to give some indication of current materials. We are happy with the main concepts behind the brochure, and would not really be looking to change the key concepts unless you have a compelling reason. We do like the use of this secondary logo in the stationary related items
I have uploaded an eps file of the logo.

```html
<!DOCTYPE html>
<html lang="en">
<head>
<meta charset="utf-8">
<title>Report Template – Title Page and Contents</title>
<link rel="stylesheet" href="https://fonts.googleapis.com/css2?family=Caladea:ital,wght@0,400;0,700;1,400&family=Open+Sans:wght@400;600&display=swap">
<style>
  :root {
    --canvas-grey: #a9b0b9;
    --page-white: #ffffff;
    --brand-navy: #1d4777;
    --brand-orange: #f7962e;
    --ink-navy: #25406b;
    --ink-soft: #7d8fae;
    --leader: #8a96ab;
  }
  * { box-sizing: border-box; margin: 0; padding: 0; }
  html, body {
    width: 1200px;
    height: 900px;
    overflow: hidden;
    background: var(--canvas-grey);
  }
  .spread {
    position: relative;
    width: 1200px;
    height: 900px;
    display: flex;
    gap: 22px;
    padding: 25px 18px;
  }
  .page {
    position: relative;
    width: 572px;
    height: 850px;
    background: var(--page-white);
    box-shadow: 0 0 0 1px #7f8791, 2px 3px 8px rgba(0,0,0,0.25);
    overflow: hidden;
  }
  .page-frame {
    position: absolute;
    inset: 0;
    width: 100%;
    height: 100%;
  }
  .page-content {
    position: absolute;
    inset: 0;
    font-family: "Caladea", "Cambria", serif;
    color: var(--ink-navy);
  }

  /* Title page */
  .cover-title {
    position: absolute;
    top: 220px;
    width: 100%;
    text-align: center;
    font-size: 46px;
    font-weight: 700;
    color: var(--brand-navy);
  }
  .cover-subtitle {
    position: absolute;
    top: 325px;
    width: 100%;
    text-align: center;
    font-size: 22px;
  }
  .cover-meta {
    position: absolute;
    top: 392px;
    width: 100%;
    list-style: none;
    text-align: center;
    font-size: 15px;
    line-height: 37px;
  }

  /* Wordmark */
  .wordmark {
    position: absolute;
    display: flex;
    align-items: center;
    gap: 10px;
    font-family: "Open Sans", "Segoe UI", sans-serif;
    font-weight: 600;
    color: var(--brand-navy);
  }
  .wordmark-square {
    background: var(--brand-navy);
    flex: none;
  }
  .wordmark--cover { left: 48px; top: 690px; font-size: 24px; }
  .wordmark--cover .wordmark-square { width: 34px; height: 34px; }
  .wordmark--contents { left: 28px; top: 770px; font-size: 17px; }
  .wordmark--contents .wordmark-square { width: 24px; height: 24px; }

  /* Contents page */
  .toc {
    position: absolute;
    left: 72px;
    top: 130px;
    width: 452px;
  }
  .toc-heading {
    font-size: 13px;
    font-weight: 700;
    color: var(--brand-navy);
    margin-bottom: 10px;
  }
  .toc-list { list-style: none; }
  .toc-entry {
    display: flex;
    align-items: baseline;
    height: 26.5px;
  }
  .toc-leader {
    flex: 1;
    margin: 0 3px;
    border-bottom: 1.5px dotted var(--leader);
    transform: translateY(-3px);
  }
  .toc-entry--level1 {
    font-size: 12px;
    font-weight: 700;
    color: var(--brand-navy);
  }
  .toc-entry--level1 .toc-leader { border-bottom-color: var(--brand-navy); }
  .toc-entry--level2 {
    font-size: 9.5px;
    color: var(--ink-soft);
  }
  .toc-entry--level3 {
    font-size: 9px;
    font-style: italic;
    color: var(--ink-soft);
    padding-left: 10px;
  }
</style>
</head>
<body>
<main class="spread">

  <section class="page page--cover">
    <svg class="page-frame" viewBox="0 0 572 850" aria-hidden="true">
      <rect x="0" y="0" width="572" height="90" fill="var(--brand-navy)"/>
      <rect x="0" y="760" width="572" height="90" fill="var(--brand-orange)"/>
      <path d="M0 100 Q0 30 70 30 H572 V732 Q572 782 522 782 H0 Z" fill="var(--page-white)"/>
    </svg>
    <div class="page-content">
      <h1 class="cover-title">Report Title</h1>
      <p class="cover-subtitle">Subtitle</p>
      <ul class="cover-meta">
        <li>Date</li>
        <li>Author</li>
        <li>Etc.</li>
      </ul>
      <div class="wordmark wordmark--cover"><span class="wordmark-square"></span>Veltra Systems</div>
    </div>
  </section>

  <section class="page page--contents">
    <svg class="page-frame" viewBox="0 0 572 850" aria-hidden="true">
      <rect x="0" y="0" width="572" height="90" fill="var(--brand-navy)"/>
      <rect x="0" y="800" width="572" height="50" fill="var(--brand-orange)"/>
      <path d="M0 100 Q0 30 70 30 H572 V785 Q572 825 532 825 H0 Z" fill="var(--page-white)"/>
    </svg>
    <div class="page-content">
      <nav class="toc">
        <h2 class="toc-heading">Table of Contents</h2>
        <ol class="toc-list">
          <li class="toc-entry toc-entry--level1"><span>Type chapter level (level 1)</span><span class="toc-leader"></span><span>1</span></li>
          <li class="toc-entry toc-entry--level2"><span>Type chapter level (level 2)</span><span class="toc-leader"></span><span>2</span></li>
          <li class="toc-entry toc-entry--level3"><span>Type chapter title (level 3)</span><span class="toc-leader"></span><span>3</span></li>
          <li class="toc-entry toc-entry--level1"><span>Type chapter level (level 1)</span><span class="toc-leader"></span><span>4</span></li>
          <li class="toc-entry toc-entry--level2"><span>Type chapter level (level 2)</span><span class="toc-leader"></span><span>5</span></li>
          <li class="toc-entry toc-entry--level3"><span>Type chapter title (level 3)</span><span class="toc-leader"></span><span>6</span></li>
        </ol>
      </nav>
      <div class="wordmark wordmark--contents"><span class="wordmark-square"></span>Veltra Systems</div>
    </div>
  </section>

</main>
</body>
</html>
```